Halvard Property Website

Our organization has multiple arms. We want a 5-page website to address the divisions of our company. Pelgrave Yards, our 1500 square foot flex office space will have 3 of those pages. We need a landing page for Halvard Property Holdings and a Contact Us page for the organization. Then the 3 pages dedicated to Pelgrave Yards: a page showing office pictures, a page for pricing, and a calendar page for this part of our business; for a total of 5 pages.
Updates

Please note, we need a logo for Pelgrave Yards (the flex office space). We have a logo for Halvard Property (see attachments). It is not a requirement for Pelgrave's logo to match Halvard's logo.

Industry/Entity Type

Real Estate

Coding

Requirements
Must have
• Domain, Email, Logo (for Pelgrave Yards),

```html
<!DOCTYPE html>
<html lang="en">
<head>
<meta charset="utf-8">
<title>Halvard Property</title>
<link href="https://fonts.googleapis.com/css2?family=Roboto:wght@300;400;500;700;900&family=Oswald:wght@600;700&display=swap" rel="stylesheet">
<style>
:root{
  --pink:#e9296f;
  --blue:#1a74bf;
  --blue-deep:#1570b8;
  --cyan:#1ec4ea;
  --lime:#b8cf14;
  --ink:#1b1b1b;
  --text:#555;
  --line:#d6d6d6;
  --footer:#232323;
  --sky:#eaf5fb;
}
*{margin:0;padding:0;box-sizing:border-box}
html,body{width:1200px;height:3728px;overflow:hidden}
body{position:relative;font-family:"Roboto",sans-serif;color:var(--ink);background:#fff}
.abs{position:absolute}
.center{text-align:center}

/* hero */
.hero{left:0;top:0;width:1200px;height:651px;background:linear-gradient(180deg,#a9cde6 0%,#d3e4ef 22%,#8e9aa6 38%,#5d6874 52%,#8d8f92 56%,#c8c9cb 75%,#a9aaac 100%)}
.brand{left:159px;top:28px;width:160px;text-align:center}
.brand-mark{width:22px;height:22px;background:var(--pink);margin:0 auto 10px}
.brand-name{font-family:"Roboto",sans-serif;font-weight:500;font-size:30px;letter-spacing:6px;color:#2a2a2a;line-height:1}
.brand-sub{font-family:"Roboto",sans-serif;font-weight:500;font-size:8px;letter-spacing:2px;color:#2a2a2a;margin-top:8px}
.nav{right:162px;top:53px;display:flex;gap:22px}
.nav a{font-size:14px;font-weight:500;color:#1b1b1b;text-decoration:none}
.hero-title{left:0;top:430px;width:1200px;font-family:"Oswald",sans-serif;font-weight:700;font-size:52px;color:#151515;letter-spacing:.5px}
.search{left:161px;top:517px;width:877px;height:79px;background:#fff;display:flex}
.field{width:249px;padding:15px 20px 0 19px;border-right:1px solid #e3e3e3}
.field label{display:block;font-size:12px;color:#222;margin-bottom:8px}
.select{height:26px;border:1px solid #cfcfcf;position:relative}
.select:after{content:"";position:absolute;right:8px;top:11px;border:4px solid transparent;border-top-color:#333}
.search-btn{margin-left:auto;width:130px;background:var(--pink);color:#fff;font-weight:700;font-size:15px;display:flex;align-items:center;justify-content:center;gap:6px}

/* explore */
.kicker{left:0;top:712px;width:1200px;font-size:12px;color:#555}
.section-title{left:0;width:1200px;font-weight:900;color:var(--ink)}
.explore-title{top:724px;font-size:37px;color:var(--blue)}
.rule{left:564px;top:772px;width:74px;height:3px;background:#222}
.tile{overflow:hidden}
.tile-photo{width:100%;height:100%}
.tile-bar{position:absolute;left:0;bottom:0;width:100%;display:flex;align-items:center;justify-content:space-between;padding:0 15px;color:#fff;font-weight:700;font-size:19px}
.tile-bar .lens{width:32px;height:32px;border-radius:50%;background:#fff;display:flex;align-items:center;justify-content:center}

/* welcome */
.welcome-photo{left:0;top:1301px;width:605px;height:534px;background:linear-gradient(180deg,#e9eaeb 0%,#b4b6b8 40%,#6a6c6e 75%,#3e4042 100%)}
.welcome-panel{left:605px;top:1301px;width:595px;height:534px;background:var(--blue-deep);color:#fff}
.welcome-kicker{top:54px;width:100%;font-size:18px;font-weight:300;letter-spacing:3px}
.welcome-title{top:74px;width:100%;font-size:39px;font-weight:900}
.welcome-copy{left:28px;width:485px;font-size:11.2px;line-height:17px;font-weight:300}
.action{display:flex;align-items:center;gap:12px;font-size:14px;font-weight:700}
.action .ibox{width:50px;height:46px;border:1.5px solid #fff;display:flex;align-items:center;justify-content:center}

/* listing */
.listing-wave{left:-200px;top:2030px;width:1600px;height:470px;border-radius:0 0 50% 50%;background:linear-gradient(180deg,#ffffff 0%,#d9eef6 100%)}
.listing-title{top:1880px;font-size:36px}
.card{width:277px;height:395px;background:#fff;box-shadow:0 1px 4px rgba(0,0,0,.08)}
.card-photo{height:168px}
.card-meta{height:40px;background:var(--blue);color:#fff;display:flex;align-items:center;justify-content:space-between;padding:0 12px;font-size:10.5px}
.card-meta b{font-size:12px}
.card-addr{font-size:14px;font-weight:700;margin-top:26px}
.card-copy{font-size:11px;line-height:17px;color:#444;padding:0 22px;margin-top:12px}
.card-foot{position:absolute;left:0;bottom:0;width:100%;height:42px;background:var(--pink);color:#fff;display:flex;align-items:center;justify-content:space-between;padding:0 12px;font-size:10px}
.arrow-btn{width:40px;height:40px;border-radius:50%;background:#d9edf4;display:flex;align-items:center;justify-content:center}

/* steps */
.steps-title{top:2536px;font-size:36px}
.steps-copy{left:250px;top:2592px;width:700px;font-size:11px;line-height:18px;color:#444}
.step{width:290px;text-align:center}
.step-circle{width:108px;height:108px;border-radius:50%;margin:0 auto;display:flex;align-items:center;justify-content:center}
.step h3{font-size:14.5px;font-weight:700;margin-top:22px}
.step p{font-size:11px;line-height:17px;color:#444;margin-top:14px}
.partner{width:169px;height:142px;border:1px solid #e2e2e2;display:flex;align-items:center;justify-content:center}
.partner span{display:block;width:70px;height:56px;border-radius:6px}

/* contact */
.map{left:0;top:3132px;width:596px;height:519px;background:linear-gradient(135deg,#f3e3a8 0%,#ead68f 50%,#f1df9f 100%)}
.city-bg{left:596px;top:3132px;width:604px;height:519px;background:linear-gradient(180deg,#eef6fb 0%,#dbeaf4 55%,#8fb0c8 100%)}
.form-card{left:683px;top:3174px;width:430px;height:477px;background:#fff}
.form-title{top:40px;width:100%;font-size:30px;font-weight:900}
.form-copy{top:88px;left:40px;width:350px;font-size:11.5px;line-height:18px;color:#444}
.input{left:38px;width:356px;height:35px;border:1px solid #cfcfcf;font-size:10.5px;color:#444;padding:12px 13px}
.submit{left:38px;top:384px;width:356px;height:45px;background:var(--pink);color:#fff;font-weight:700;font-size:19px;display:flex;align-items:center;justify-content:center}

/* footer */
.footer{left:0;top:3651px;width:1200px;height:77px;background:var(--footer);color:#ddd}
.copyright{left:161px;top:31px;font-size:12px}
.social{left:902px;top:24px;display:flex;gap:7px}
.social span{width:28px;height:28px;border-radius:50%;border:1.5px solid #ddd}
</style>
</head>
<body>

<!-- hero -->
<header class="abs hero" role="img" aria-label="City skyline above a paved plaza"></header>
<div class="abs brand">
  <div class="brand-mark"></div>
  <div class="brand-name">HALVARD</div>
  <div class="brand-sub">PROPERTY HOLDINGS</div>
</div>
<nav class="abs nav">
  <a>HOME</a><a>PELGRAVE YARDS</a><a>PRICING</a><a>CALENDAR</a><a>CONTACT US</a>
</nav>
<h1 class="abs hero-title center">FIND YOUR DREAM HOME</h1>
<form class="abs search">
  <div class="field"><label>Main Location</label><div class="select"></div></div>
  <div class="field"><label>Property Status</label><div class="select"></div></div>
  <div class="field"><label>Property Type</label><div class="select"></div></div>
  <div class="search-btn">
    <svg width="15" height="15" viewBox="0 0 16 16"><circle cx="6.5" cy="6.5" r="4.8" fill="none" stroke="#fff" stroke-width="2.2"/><line x1="10" y1="10" x2="14.5" y2="14.5" stroke="#fff" stroke-width="2.4"/></svg>SEARCH
  </div>
</form>

<!-- explore -->
<svg class="abs" style="left:591px;top:691px" width="20" height="12" viewBox="0 0 20 12"><polyline points="2,10 10,2 18,10" fill="none" stroke="var(--pink)" stroke-width="2.4"/></svg>
<div class="abs kicker center">FIND PROPERTY IN YOUR CITY</div>
<h2 class="abs section-title explore-title center">EXPLORE PROPERTY</h2>
<div class="abs rule"></div>

<div class="abs tile" style="left:161px;top:815px;width:434px;height:425px">
  <div class="tile-photo" role="img" aria-label="Modern two-storey family house with lawn" style="background:linear-gradient(180deg,#a9cbe8 0%,#dfe6ec 35%,#8b7d6f 65%,#6d8a3a 100%)"></div>
  <div class="tile-bar" style="height:58px;background:var(--pink)">RESIDENTIAL<span class="lens"><svg width="16" height="16" viewBox="0 0 16 16"><circle cx="6.5" cy="6.5" r="4.5" fill="none" stroke="var(--pink)" stroke-width="2"/><line x1="10" y1="10" x2="14" y2="14" stroke="var(--pink)" stroke-width="2.2"/></svg></span></div>
</div>
<div class="abs tile" style="left:612px;top:815px;width:426px;height:208px">
  <div class="tile-photo" role="img" aria-label="Aerial view of dense city towers" style="background:linear-gradient(180deg,#8fb2d0 0%,#6a7a8c 50%,#4a5968 100%)"></div>
  <div class="tile-bar" style="height:46px;background:rgba(30,196,234,.92)">COMMERCIAL<span class="lens"><svg width="16" height="16" viewBox="0 0 16 16"><circle cx="6.5" cy="6.5" r="4.5" fill="none" stroke="var(--cyan)" stroke-width="2"/><line x1="10" y1="10" x2="14" y2="14" stroke="var(--cyan)" stroke-width="2.2"/></svg></span></div>
</div>
<div class="abs tile" style="left:612px;top:1039px;width:201px;height:201px">
  <div class="tile-photo" role="img" aria-label="Office meeting room with table and chairs" style="background:linear-gradient(180deg,#f2f2f2 0%,#cfcfcf 55%,#3a3a3a 100%)"></div>
  <div class="tile-bar" style="height:58px;background:rgba(184,207,20,.95)">OFFICE<span class="lens"><svg width="16" height="16" viewBox="0 0 16 16"><circle cx="6.5" cy="6.5" r="4.5" fill="none" stroke="var(--lime)" stroke-width="2"/><line x1="10" y1="10" x2="14" y2="14" stroke="var(--lime)" stroke-width="2.2"/></svg></span></div>
</div>
<div class="abs tile" style="left:828px;top:1039px;width:210px;height:201px">
  <div class="tile-photo" role="img" aria-label="Skyscrapers on a waterfront" style="background:linear-gradient(180deg,#5d8fc7 0%,#7ea5cf 50%,#3e4e62 100%)"></div>
  <div class="tile-bar" style="height:56px;background:rgba(26,116,191,.93)">INDUSTRIAL<span class="lens"><svg width="16" height="16" viewBox="0 0 16 16"><circle cx="6.5" cy="6.5" r="4.5" fill="none" stroke="var(--blue)" stroke-width="2"/><line x1="10" y1="10" x2="14" y2="14" stroke="var(--blue)" stroke-width="2.2"/></svg></span></div>
</div>

<!-- welcome -->
<div class="abs welcome-photo" role="img" aria-label="Black and white city towers and an elevated roadway"></div>
<section class="abs welcome-panel">
  <div class="abs welcome-kicker center">WELCOME TO</div>
  <h2 class="abs welcome-title center">HALVARD PROPERTY</h2>
  <p class="abs welcome-copy center" style="top:132px">Lorem Ipsum is simply dummy text of the printing and typesetting industry. when an unknown printer took a galley of type and scrambled it to make a type specimen book. It has survived not only five centuries, but also the leap into electronic typesetting, remaining essentially unchanged. It was popularisedLetraset sheets containing Lorem Ipsum passages, and more recently with desktop pub Maker including versions of Lorem Ipsum.</p>
  <p class="abs welcome-copy center" style="top:249px">Lorem Ipsum is simply dummy text of the printing and typesetting industry. specimen book. It has survived not only five centuries, but also the leap into electronic typesetting, remaining essentially unchanged. It was popularisedLetraset sheets containing Lorem Ipsum passages, Maker including versions</p>
  <div class="abs action" style="left:30px;top:353px"><span class="ibox"><svg width="28" height="26" viewBox="0 0 28 26" fill="none" stroke="#fff" stroke-width="1.6"><polyline points="4,12 14,3 24,12"/><rect x="8" y="11" width="12" height="12"/></svg></span>BUY PROPERTIES</div>
  <div class="abs action" style="left:247px;top:353px">SELL PROPERTIES<span class="ibox"><svg width="28" height="26" viewBox="0 0 28 26" fill="none" stroke="#fff" stroke-width="1.6"><circle cx="17" cy="8" r="5"/><path d="M3 20h7l6 3 9-6"/></svg></span></div>
  <div class="abs action" style="left:30px;top:434px"><span class="ibox"><svg width="28" height="26" viewBox="0 0 28 26" fill="none" stroke="#fff" stroke-width="1.6"><circle cx="9" cy="9" r="5"/><line x1="13" y1="13" x2="24" y2="22"/><line x1="20" y1="18" x2="17" y2="21"/></svg></span>RENT PROPERTIES</div>
  <div class="abs action" style="left:252px;top:434px">FIND PROPERTIES<span class="ibox"><svg width="28" height="26" viewBox="0 0 28 26" fill="none" stroke="#fff" stroke-width="1.6"><circle cx="12" cy="11" r="7"/><line x1="17" y1="16" x2="24" y2="23"/></svg></span></div>
</section>

<!-- listing -->
<div class="abs listing-wave"></div>
<h2 class="abs section-title listing-title center">PROPERTY LISTING</h2>
<div class="abs arrow-btn" style="left:96px;top:2135px"><svg width="12" height="16" viewBox="0 0 12 16"><polyline points="9,2 3,8 9,14" fill="none" stroke="#8aa" stroke-width="2.4"/></svg></div>
<div class="abs arrow-btn" style="left:1064px;top:2135px"><svg width="12" height="16" viewBox="0 0 12 16"><polyline points="3,2 9,8 3,14" fill="none" stroke="#8aa" stroke-width="2.4"/></svg></div>

<article class="abs card center" style="left:161px;top:1963px">
  <div class="card-photo" role="img" aria-label="Apartment blocks along a garden path" style="background:linear-gradient(180deg,#8bbbe6 0%,#c9d3da 50%,#7d8f55 100%)"></div>
  <div class="card-meta"><span>&#9679; Lorem Ipsum simply dummy text</span><b>$479,500</b></div>
  <div class="card-addr">154 23 AV NW</div>
  <p class="card-copy">Lorem Ipsum is simply dummy text best printing and typesetting industry. Lorem Ipsum has been the industry's standard dummy</p>
  <div class="card-foot"><span>870 ft2</span><span>2 bedrooms</span><span>2 baths</span></div>
</article>
<article class="abs card center" style="left:462px;top:1963px">
  <div class="card-photo" role="img" aria-label="Suburban house with garage at dusk" style="background:linear-gradient(180deg,#6e99c8 0%,#b5b0a6 55%,#7b7a72 100%)"></div>
  <div class="card-meta"><span>&#9679; Lorem Ipsum simply dummy text</span><b>$479,500</b></div>
  <div class="card-addr">154 23 AV NW</div>
  <p class="card-copy">Lorem Ipsum is simply dummy text best printing and typesetting industry. Lorem Ipsum has been the industry's standard dummy</p>
  <div class="card-foot"><span>870 ft2</span><span>2 bedrooms</span><span>2 baths</span></div>
</article>
<article class="abs card center" style="left:761px;top:1963px">
  <div class="card-photo" role="img" aria-label="White modern apartment building" style="background:linear-gradient(180deg,#8ec1ea 0%,#e9ebea 50%,#a8b0a4 100%)"></div>
  <div class="card-meta"><span>&#9679; Lorem Ipsum simply dummy text</span><b>$479,500</b></div>
  <div class="card-addr">154 23 AV NW</div>
  <p class="card-copy">Lorem Ipsum is simply dummy text best printing and typesetting industry. Lorem Ipsum has been the industry's standard dummy</p>
  <div class="card-foot"><span>870 ft2</span><span>2 bedrooms</span><span>2 baths</span></div>
</article>

<!-- steps -->
<h2 class="abs section-title steps-title center">SIMPLE STEPS</h2>
<p class="abs steps-copy center">Lorem Ipsum is simply dummy text of the printing and typesetting industry. Lorem Ipsum has been the industry's standard dummy text when an unknown printer took a galley of type and scrambled it to make a type specimen book.</p>

<div class="abs step" style="left:147px;top:2657px">
  <div class="step-circle" style="background:var(--lime)"><svg width="56" height="56" viewBox="0 0 56 56" fill="none" stroke="#fff" stroke-width="2.4"><polyline points="8,26 28,9 48,26"/><polyline points="14,22 14,46 42,46 42,22"/><circle cx="28" cy="32" r="7"/><line x1="33" y1="37" x2="38" y2="42"/></svg></div>
  <h3>Search For Real Estates</h3>
  <p>Lorem Ipsum is simply dummy text of the printing typesetting industry. Lorem Ipsum has been industry standard dummy text</p>
</div>
<div class="abs step" style="left:455px;top:2657px">
  <div class="step-circle" style="background:var(--pink)"><svg width="56" height="56" viewBox="0 0 56 56" fill="none" stroke="#fff" stroke-width="2.4"><polyline points="8,26 28,9 48,26"/><polyline points="14,22 14,46 42,46 42,22"/><path d="M28 40c-8-6-9-9-7-12 2-2 5-2 7 1 2-3 5-3 7-1 2 3 1 6-7 12z"/></svg></div>
  <h3>Select Your Favorite</h3>
  <p>Lorem Ipsum is simply dummy text of the printing typesetting industry. Lorem Ipsum has been industry standard dummy text</p>
</div>
<div class="abs step" style="left:761px;top:2657px">
  <div class="step-circle" style="background:var(--cyan)"><svg width="56" height="56" viewBox="0 0 56 56" fill="none" stroke="#fff" stroke-width="2.4"><polyline points="6,24 24,9 42,24"/><polyline points="11,20 11,44 28,44"/><circle cx="38" cy="32" r="7"/><line x1="33" y1="37" x2="24" y2="46"/><line x1="27" y1="43" x2="30" y2="46"/></svg></div>
  <h3>Take Your Key</h3>
  <p>Lorem Ipsum is simply dummy text of the printing typesetting industry. Lorem Ipsum has been industry standard dummy text</p>
</div>

<svg class="abs" style="left:128px;top:2985px" width="14" height="20" viewBox="0 0 14 20"><polyline points="11,2 3,10 11,18" fill="none" stroke="#bbb" stroke-width="2.4"/></svg>
<svg class="abs" style="left:1061px;top:2985px" width="14" height="20" viewBox="0 0 14 20"><polyline points="3,2 11,10 3,18" fill="none" stroke="#bbb" stroke-width="2.4"/></svg>
<div class="abs partner" style="left:161px;top:2921px"><span style="background:#2a6fb0"></span></div>
<div class="abs partner" style="left:338px;top:2921px"><span style="background:#f26722"></span></div>
<div class="abs partner" style="left:515px;top:2921px"><span style="background:#1f3550"></span></div>
<div class="abs partner" style="left:692px;top:2921px"><span style="background:#d3263a"></span></div>
<div class="abs partner" style="left:869px;top:2921px"><span style="background:#1e3e6d"></span></div>

<!-- contact -->
<div class="abs map" role="img" aria-label="Street map of the city neighbourhood"></div>
<div class="abs city-bg" role="img" aria-label="Pale city skyline"></div>
<form class="abs form-card">
  <h2 class="abs form-title center">READY TO GET STARTED?</h2>
  <p class="abs form-copy center">Please complete the form below and our agents will get right back to you in less than 24h.</p>
  <div class="abs input" style="top:141px">Your Name</div>
  <div class="abs input" style="top:187px">Your Email</div>
  <div class="abs input" style="top:233px">Your Phone</div>
  <div class="abs input" style="top:280px;height:87px">Type your message..</div>
  <div class="abs submit">SUBMIT NOW</div>
</form>

<!-- footer -->
<footer class="abs footer">
  <div class="abs copyright">© 2022 halvardproperty.com. All rights reserved.</div>
  <div class="abs social"><span></span><span></span><span></span><span></span></div>
</footer>

</body>
</html>
```